Help our Crumb Parlour find our winning design! We're looking for a business card....

We’re a Crumb Parlour in NY specializing in custom-made cakes and unique desserts.
Our cakes combine flavor and art, each designed to match customer’s special event and theme.
We’d like a unique business card with a clean design that will combine French chic and artistic look & feel.
We’d like to differentiate ourselves from standard bakeries, please don’t offer cupcake images :-)
Our logo is peach-pink and brown and we’d love to use these colors ( . Another color that can be added is gold - or feel free to suggest!

Target Market(s)

Women, ages 25-55

Industry/Entity Type

Boutique

Contact Information for Business Card

Text on card:
Logo
Crumb Parlour by Dana Whitfield

www.xxxxxxxx.com
xxx@xxxxx.com
(516) xxx-xxxx
F – xxxxxxxxxx
IG - xxxxxxxxx

Font styles to use
Sans Serif
Script

Requirements
Must have
• Logo
• Clean look
• French chic and artistic look & feel.
Nice to have
• Damask pattern
Should not have
• Cupcake images

```html
<!DOCTYPE html>
<html lang="en">
<head>
<meta charset="utf-8">
<title>Crumb Parlour — Business Card</title>
<link href="https://fonts.googleapis.com/css2?family=Great+Vibes&family=Lato:wght@400;700&family=Tinos&display=swap" rel="stylesheet">
<style>
  :root {
    --backdrop: #aaaaaa;
    --card: #ffffff;
    --brown: #2a1b1c;
    --brown-soft: #4a3a3b;
    --peach: #dca99f;
    --ink: #231a1a;
  }
  * { margin: 0; padding: 0; box-sizing: border-box; }
  html, body { width: 1200px; height: 852px; overflow: hidden; }
  body {
    background: var(--backdrop);
    position: relative;
    color: var(--ink);
  }
  .card {
    position: absolute;
    top: 276px;
    width: 525px;
    height: 300px;
    background: var(--card);
    border-radius: 28px;
    overflow: hidden;
  }
  .card--front { left: 50px; }
  .card--back { left: 625px; }

  .card__band {
    position: absolute;
    left: 0; right: 0; bottom: 0;
    height: 42px;
    background: linear-gradient(180deg, var(--brown-soft), var(--brown));
  }
  .card__band::after {
    content: "";
    position: absolute;
    top: 0; right: 0; bottom: 0;
    width: 112px;
    background: var(--peach);
    clip-path: polygon(22px 0, 100% 0, 100% 100%, 0 100%);
  }

  .brand {
    position: absolute;
    display: flex;
    align-items: center;
    gap: 10px;
    font-family: "Lato", sans-serif;
    font-weight: 700;
    font-size: 26px;
    letter-spacing: 4px;
    text-transform: uppercase;
    color: var(--brown);
  }
  .brand__dot {
    width: 12px; height: 12px;
    border-radius: 50%;
    background: var(--peach);
  }
  .card--front .brand { left: 0; right: 0; top: 110px; justify-content: center; }
  .card--back .brand { left: 40px; top: 78px; font-size: 21px; letter-spacing: 3px; }

  .owner {
    position: absolute;
    right: 34px;
    top: 30px;
    text-align: center;
  }
  .owner__title {
    font-family: "Lato", sans-serif;
    font-size: 15px;
    letter-spacing: 0.3px;
  }
  .owner__name {
    font-family: "Great Vibes", cursive;
    font-size: 34px;
    line-height: 1;
  }

  .social {
    position: absolute;
    right: 30px;
    top: 140px;
    list-style: none;
    font-family: "Tinos", serif;
    font-size: 14px;
  }
  .social li { display: flex; align-items: center; gap: 10px; margin-bottom: 4px; }
  .social__mark { width: 10px; height: 10px; background: var(--ink); border-radius: 2px; }

  .contact {
    position: absolute;
    left: 38px;
    bottom: 58px;
    list-style: none;
    font-family: "Tinos", serif;
    font-size: 15px;
  }
  .contact li { display: flex; align-items: center; gap: 12px; line-height: 20px; }
  .contact svg { width: 14px; height: 14px; fill: var(--ink); }
</style>
</head>
<body>

<section class="card card--front" aria-label="Business card front">
  <div class="brand"><span class="brand__dot"></span>Sugar Reverie</div>
  <div class="card__band"></div>
</section>

<section class="card card--back" aria-label="Business card back">
  <div class="brand"><span class="brand__dot"></span>Sugar Reverie</div>

  <div class="owner">
    <p class="owner__title">Crumb Parlour by</p>
    <p class="owner__name">Dana Whitfield</p>
  </div>

  <ul class="social">
    <li><span class="social__mark"></span>SugarReverieNYCakes</li>
    <li><span class="social__mark"></span>SugarReverieNYCakes</li>
  </ul>

  <ul class="contact">
    <li>
      <svg viewBox="0 0 16 16" aria-hidden="true"><path d="M3 2h3l1.5 3.5-2 1.2a8 8 0 0 0 3.8 3.8l1.2-2L14 10v3a1 1 0 0 1-1 1A12 12 0 0 1 2 3a1 1 0 0 1 1-1z"/></svg>
      (516) 555-0182
    </li>
    <li>
      <svg viewBox="0 0 16 16" aria-hidden="true"><path d="M1 3h14v10H1z M2 4.2v.3l6 4 6-4v-.3z" fill-rule="evenodd"/></svg>
      www.SugarReverieNY.com
    </li>
    <li>
      <svg viewBox="0 0 16 16" aria-hidden="true"><path d="M8 1a7 7 0 1 0 0 14A7 7 0 0 0 8 1zm0 1.5c.8 0 1.7 1.6 2 4H6c.3-2.4 1.2-4 2-4zM2.6 7h2.4a13 13 0 0 0 0 2H2.6a5.5 5.5 0 0 1 0-2zm8.4 0h2.4a5.5 5.5 0 0 1 0 2H11a13 13 0 0 0 0-2zM6 9.5h4c-.3 2.4-1.2 4-2 4s-1.7-1.6-2-4z"/></svg>
      dana@SugarReverieNY.com
    </li>
  </ul>

  <div class="card__band"></div>
</section>

</body>
</html>
```